Business Card Design- Mortgage Firm

Looking to design a business Card for our Outside sales people. This card is used to provide their contact information to prospective clients and realtors. Must have All Pertinent company and licensing information by law. We are looking for a very modern design that flows with our current logo color scheme. Red/White/Black

Industry/Entity Type

Mortgage Lender

Contact Information for Business Card

Must stick with current color scheme.

Colors
f04a50
ffffff
ecf7fb

Requirements
Must have
• Company Logo or similar
• Company Address (748 W Alder Avenue, Suite 312, Elm Vale CA 92879 NMLS: 4072916)
• Agent Name (Mira Talbot)
• Title (Senior Mortgage Loan Originator)
• NMLS# 8395021
• Toll Free: 800-627-3184
• Direct : 310-555-4860
Nice to have
• Room for Agent Picture

```html
<!DOCTYPE html>
<html lang="en">
<head>
<meta charset="utf-8">
<title>Brightwell Mortgage – Business Card</title>
<link href="https://fonts.googleapis.com/css2?family=Lato:wght@400;700;900&display=swap" rel="stylesheet">
<style>
  :root {
    --brand-red: #b91f26;
    --text-red: #b8242a;
    --ink: #141414;
    --white: #ffffff;
    --card-tint: #eeeeef;
    --stage: #e7e4df;
    --photo-top: #c9d3de;
    --photo-bottom: #5f87c2;
  }
  * { margin: 0; padding: 0; box-sizing: border-box; }
  html, body { width: 900px; height: 1200px; overflow: hidden; }
  body {
    background: var(--stage);
    font-family: "Lato", Arial, sans-serif;
    position: relative;
  }
  .card {
    position: absolute;
    left: 82px;
    width: 733px;
    height: 428px;
    border-radius: 22px;
    overflow: hidden;
    box-shadow: 0 6px 16px rgba(0,0,0,.25);
  }
  .card--front {
    top: 137px;
    background: linear-gradient(180deg, var(--white) 0%, var(--white) 55%, var(--card-tint) 100%);
  }
  .card--back {
    top: 632px;
    background: var(--brand-red);
  }
  .front-band {
    position: absolute;
    left: 0; bottom: 0;
    width: 733px; height: 30px;
  }
  .agent-photo {
    position: absolute;
    left: 468px; top: 18px;
    width: 250px; height: 382px;
    background: linear-gradient(180deg, var(--photo-top) 0%, var(--photo-bottom) 100%);
  }
  .wordmark {
    position: absolute;
    display: flex;
    align-items: center;
    gap: 14px;
    color: var(--text-red);
  }
  .wordmark__square {
    width: 62px; height: 62px;
    background: currentColor;
    flex: none;
  }
  .wordmark__name {
    font-weight: 700;
    font-size: 42px;
    line-height: 1.05;
    letter-spacing: 3px;
    text-transform: uppercase;
    white-space: nowrap;
  }
  .card--front .wordmark { left: 34px; top: 48px; }
  .card--back .wordmark {
    color: var(--white);
    left: 0; right: 0; top: 162px;
    justify-content: center;
  }
  .agent-name {
    position: absolute;
    left: 45px; top: 155px;
    font-size: 24px; font-weight: 900;
    color: var(--ink); letter-spacing: .5px;
  }
  .agent-role {
    position: absolute;
    left: 45px; top: 184px;
    font-size: 17px; line-height: 25px;
    color: var(--text-red);
  }
  .rule {
    position: absolute;
    left: 45px; width: 369px; height: 1.5px;
    background: var(--ink);
  }
  .rule--top { top: 237px; }
  .rule--bottom { top: 346px; }
  .contact-list {
    position: absolute;
    left: 45px; top: 247px;
    list-style: none;
  }
  .contact-list li {
    display: flex; align-items: center;
    height: 22.5px;
    font-size: 16px; color: var(--ink);
  }
  .contact-list svg { width: 17px; height: 17px; margin-right: 10px; flex: none; }
  .office-address {
    position: absolute;
    left: 45px; top: 352px;
    font-size: 16px; line-height: 25px; color: var(--ink);
    font-style: normal;
    white-space: nowrap;
  }
</style>
</head>
<body>

<section class="card card--front" aria-label="Business card front">
  <div class="agent-photo" role="img" aria-label="Portrait photo of the loan originator in a blue shirt and red tie"></div>

  <svg class="front-band" viewBox="0 0 733 30" aria-hidden="true">
    <path d="M0 6 H460 L478 0 H733 V30 H0 Z" fill="var(--brand-red)"/>
  </svg>

  <div class="wordmark">
    <span class="wordmark__square"></span>
    <span class="wordmark__name">Brightwell<br>Mortgage</span>
  </div>

  <h1 class="agent-name">MIRA TALBOT</h1>
  <p class="agent-role">Senior Mortgage Loan Originator<br>NMLS# 8395021</p>

  <div class="rule rule--top"></div>
  <ul class="contact-list">
    <li>
      <svg viewBox="0 0 17 17" aria-hidden="true"><rect width="17" height="17" rx="3" fill="var(--text-red)"/><path d="M5 3.5 L7 6 L6 7.3 Q7.5 9.8 9.8 11 L11 10 L13.5 12 L12.2 13.6 Q7.5 13 3.5 5 Z" fill="#fff"/></svg>
      Toll Free: 800-627-3184
    </li>
    <li>
      <svg viewBox="0 0 17 17" aria-hidden="true"><rect width="17" height="17" rx="3" fill="var(--text-red)"/><path d="M5 3.5 L7 6 L6 7.3 Q7.5 9.8 9.8 11 L11 10 L13.5 12 L12.2 13.6 Q7.5 13 3.5 5 Z" fill="#fff"/></svg>
      Direct : 310-555-4860
    </li>
    <li>
      <svg viewBox="0 0 17 17" aria-hidden="true"><rect width="17" height="17" rx="3" fill="var(--text-red)"/><rect x="5" y="3" width="7" height="4" fill="#fff"/><rect x="3" y="7.5" width="11" height="5" rx="1" fill="#fff"/><rect x="5" y="11" width="7" height="3" fill="#fff"/></svg>
      888-903-2715
    </li>
    <li>
      <svg viewBox="0 0 17 17" aria-hidden="true"><rect width="17" height="17" rx="3" fill="var(--text-red)"/><circle cx="8.5" cy="8.5" r="5" fill="none" stroke="#fff" stroke-width="1.3"/><path d="M3.5 8.5 H13.5 M8.5 3.5 Q5.5 8.5 8.5 13.5 M8.5 3.5 Q11.5 8.5 8.5 13.5" fill="none" stroke="#fff" stroke-width="1"/></svg>
      www.brightwellmortgage.com
    </li>
  </ul>
  <div class="rule rule--bottom"></div>

  <address class="office-address">
    (748 W Alder Avenue, Suite 312, Elm Vale CA 92879<br>NMLS: 4072916)
  </address>
</section>

<section class="card card--back" aria-label="Business card back">
  <div class="wordmark">
    <span class="wordmark__square"></span>
    <span class="wordmark__name">Brightwell<br>Mortgage</span>
  </div>
</section>

</body>
</html>
```